Bref créative
Brightwave IT Business cards
Professional
Kenneth Darrow
Chief Information Officer
248 Maple Hollow Rd
KDarrow@BrightwaveIT.example
www.brightwaveit.example
IT managed services
Managed backups
Web Hosting
Email Hosting
Spam Filtering
Networking
Structured Cabling
Project Planning
Colocation Services

```html
<!DOCTYPE html>
<html lang="en">
<head>
<meta charset="utf-8">
<title>Brightwave IT – Business Cards</title>
<link rel="stylesheet" href="https://fonts.googleapis.com/css2?family=Arimo:ital,wght@0,400;0,700;1,400&display=swap">
<style>
  :root {
    --page: #ffffff;
    --brand-blue: #1e7fd0;
    --deep-blue: #0d5fa8;
    --ink: #2b2b2b;
    --grey-light: #f2f2f3;
    --grey-mid: #c9cacd;
    --grey-dark: #9a9ba0;
    --card-edge: #d6d6d8;
  }
  * { margin: 0; padding: 0; box-sizing: border-box; }
  html, body {
    width: 1200px; height: 523px; overflow: hidden;
    background: var(--page);
    font-family: "Arimo", Arial, sans-serif;
  }
  .sheet { position: relative; width: 1200px; height: 523px; }
  .card {
    position: absolute; top: 103px;
    width: 482px; height: 300px;
    border: 1px solid var(--card-edge);
    overflow: hidden;
  }
  .card--front { left: 89px; }
  .card--back { left: 619px; }
  .card__art { position: absolute; inset: 0; width: 100%; height: 100%; }

  .brand {
    position: absolute; left: 30px; top: 32px;
    display: flex; align-items: center; gap: 9px;
  }
  .brand__dot {
    width: 26px; height: 26px; border-radius: 50%;
    background: var(--brand-blue);
  }
  .brand__name {
    font-size: 30px; font-weight: 700; color: var(--brand-blue);
    letter-spacing: 0.2px;
  }

  .person { position: absolute; left: 30px; top: 142px; }
  .person__name { font-size: 17px; font-weight: 700; color: var(--deep-blue); }
  .person__title { font-size: 12px; font-style: italic; color: var(--ink); margin-top: 3px; }

  .contact {
    position: absolute; left: 30px; top: 216px;
    font-size: 10.5px; color: var(--ink); line-height: 16px;
    border-collapse: collapse;
  }
  .contact th { text-align: left; font-weight: 700; color: var(--deep-blue); padding-right: 8px; }
  .contact td { font-weight: 400; }

  .services {
    position: absolute; left: 322px; top: 170px;
    list-style: none; font-size: 10px; color: var(--ink); line-height: 19px;
  }
  .services li { display: flex; align-items: center; gap: 6px; }
  .services li::before {
    content: ""; width: 7px; height: 7px;
    background: var(--brand-blue); flex: none;
  }
</style>
</head>
<body>
<main class="sheet">

  <section class="card card--front" aria-label="Business card front">
    <svg class="card__art" viewBox="0 0 482 300" preserveAspectRatio="none" aria-hidden="true">
      <defs>
        <linearGradient id="frontGrey" x1="0" y1="0" x2="1" y2="1">
          <stop offset="0" stop-color="var(--grey-light)"/>
          <stop offset="0.55" stop-color="var(--grey-mid)"/>
          <stop offset="1" stop-color="var(--grey-dark)"/>
        </linearGradient>
      </defs>
      <rect width="482" height="300" fill="url(#frontGrey)"/>
      <path d="M0 0 H482 V12 C340 40 300 128 0 124 Z" fill="#ffffff"/>
      <path d="M0 124 C300 128 340 40 482 12" fill="none" stroke="var(--brand-blue)" stroke-width="4"/>
      <path d="M0 131 C305 135 345 48 482 20" fill="none" stroke="#ffffff" stroke-width="1.5" opacity="0.85"/>
    </svg>

    <div class="brand">
      <span class="brand__dot"></span>
      <span class="brand__name">Brightwave IT</span>
    </div>

    <div class="person">
      <p class="person__name">Kenneth Darrow</p>
      <p class="person__title">Chief Information Officer</p>
    </div>

    <table class="contact">
      <tr><th>Address :</th><td>248 Maple Hollow Rd</td></tr>
      <tr><th>Phone :</th><td>512-555-0143</td></tr>
      <tr><th>Email :</th><td>KDarrow@BrightwaveIT.example</td></tr>
      <tr><th>Website :</th><td>www.brightwaveit.example</td></tr>
    </table>

    <ul class="services">
      <li>IT managed services</li>
      <li>Managed backups</li>
      <li>Web Hosting</li>
      <li>Email Hosting</li>
      <li>Spam Filtering</li>
      <li>Colocation Services</li>
    </ul>
  </section>

  <section class="card card--back" aria-label="Business card back">
    <svg class="card__art" viewBox="0 0 482 300" preserveAspectRatio="none" aria-hidden="true">
      <defs>
        <linearGradient id="backGrey" x1="0" y1="0" x2="1" y2="1">
          <stop offset="0" stop-color="var(--grey-dark)"/>
          <stop offset="1" stop-color="var(--grey-light)"/>
        </linearGradient>
        <linearGradient id="backGrey2" x1="1" y1="1" x2="0" y2="0">
          <stop offset="0" stop-color="var(--grey-dark)"/>
          <stop offset="1" stop-color="var(--grey-light)"/>
        </linearGradient>
      </defs>
      <rect width="482" height="300" fill="#ffffff"/>
      <path d="M0 0 H100 C40 40 8 130 0 257 Z" fill="url(#backGrey)"/>
      <path d="M100 0 C40 40 8 130 0 257" fill="none" stroke="var(--brand-blue)" stroke-width="3.5"/>
      <path d="M482 300 H329 C420 270 470 190 482 100 Z" fill="url(#backGrey2)"/>
      <path d="M329 300 C420 270 470 190 482 100" fill="none" stroke="var(--brand-blue)" stroke-width="3.5"/>
    </svg>
  </section>

</main>
</body>
</html>
```